Post Card Mailer Design-

Harbridge Elder Homes is a subsidiary of the Talmont Wellness Partners. This Post Card is specifically for the Harbridge Elder Homes company and brand. Create a 4 x 6, front and back, Post Card. This Post Card will be an invitation to prospective clients and/or caring family members to join us for informative and personalized get together(s) to discuss the Senior Care Home that we are opening. It is a modern and state of the art home. Like the home, the Post Card must be eye catching, unique in its deliverables (as it doesn’t feel like a care facility) and demonstrate both attention to detail and comfort. Our organization is sophisticated and built around warmth, care and individualized personal attention. The most important aspect of this design is to focus on creating a nurturing, warm, and inviting feel that would attract a prospective client to want to join us for an educational event.

I am open to the creativity of the designer to develop something based on the above criteria; however I would like the design to work well with our existing collateral material. What I mean by that is that while I want everything to have its own personality and stand out as its own brand representative, I still need to be able to tell that the overall design concept stays stylistically inside of the same ‘family’ of existing designed material. Because of this, I would like for the designer to pull inspiration from the link to our website (Located below) as well as from our recently refreshed business cards (Attached Below). This should allow the Post Card design to be unique and creative, while still staying inside of a framework and the feel/style that I am looking for.

Finally, I want all the designers to understand that this Post Card design is for an educational and informative, small sized event where we are looking to attract attendance from prospective clients and/or caring family members of active, positive, and happy seniors/elders. We are responsible for providing personalized care for a culturally and ethnically diverse make-up of active, positive, and happy seniors/elders. The photos that are used must be tasteful, graceful, and elegant.
Updates

Industry/Entity Type

It Company

Requirements
Must have
• • The company logo must be included.•
• Look under the Harbridge Elder Homes tab at www.talmontwellpartners.example.

```html
<!DOCTYPE html>
<html lang="en">
<head>
<meta charset="utf-8">
<title>Harbridge Elder Homes – Postcard Mailer</title>
<link href="https://fonts.googleapis.com/css2?family=Montserrat:wght@400;500;700;800&display=swap" rel="stylesheet">
<style>
  :root{
    --stage:#4a4a4a;
    --paper:#ffffff;
    --ink:#1f4b45;
    --teal:#4f9a95;
    --text:#3a3a3a;
    --rule:#9a9a9a;
    --photo-warm-a:#8a6a4c;
    --photo-warm-b:#d9c2a0;
    --photo-room-a:#6b4f3a;
    --photo-room-b:#c9a987;
    --stamp:#efe9ee;
  }
  *{margin:0;padding:0;box-sizing:border-box}
  html,body{width:1200px;height:546px;overflow:hidden}
  body{background:var(--stage);font-family:"Montserrat",sans-serif;position:relative}
  .card{position:absolute;top:30px;width:563px;height:398px;background:var(--paper);overflow:hidden;box-shadow:0 6px 14px rgba(0,0,0,.35)}
  .card--front{left:27px}
  .card--back{left:610px}
  .card svg.shapes{position:absolute;inset:0}
  .headline{position:absolute;top:26px;left:30px;right:30px;text-align:center;color:var(--ink);font-weight:800;font-size:17.5px;line-height:22px;text-transform:uppercase;letter-spacing:.2px}
  .intro{position:absolute;left:20px;top:156px;width:240px;color:#fff;font-size:11.3px;line-height:15px}
  .brand{position:absolute;color:var(--teal);font-weight:500;line-height:1.1;display:flex;align-items:center;gap:8px}
  .brand__mark{width:14px;height:14px;background:var(--teal);flex:none}
  .card--front .brand{left:22px;top:318px;font-size:19px}
  .card--back .brand{left:18px;top:302px;font-size:14px}
  .tagline{position:absolute;left:30px;top:196px;width:250px;text-align:center;color:var(--text);font-size:12.5px;line-height:17px}
  .contact{position:absolute;left:140px;top:306px;width:160px;text-align:center;color:var(--text);font-size:10.5px;line-height:14.5px;font-style:normal}
  .stamp{position:absolute;left:386px;top:24px;width:148px;height:92px;background:var(--stamp)}
  .stamp__art{position:absolute;left:93px;top:6px;width:38px;height:48px;background:linear-gradient(160deg,#8a6aa8,#5e4580)}
  .postmark{position:absolute;inset:0}
  .address-lines{position:absolute;left:310px;top:207px;width:214px}
  .address-lines span{display:block;height:25px;border-bottom:1px solid var(--rule)}
</style>
</head>
<body>

<section class="card card--front">
  <svg class="shapes" width="563" height="398" viewBox="0 0 563 398">
    <defs>
      <linearGradient id="bedroom" x1="0" y1="0" x2="1" y2="1">
        <stop offset="0" stop-color="var(--photo-warm-a)"/>
        <stop offset="1" stop-color="var(--photo-warm-b)"/>
      </linearGradient>
    </defs>
    <rect width="563" height="398" fill="url(#bedroom)" role="img" aria-label="Photo: a caregiver guiding a senior woman through a stretching exercise on a ball in a bright bedroom"/>
    <path d="M0,66 C43,84 144,96 214,112 C254,124 274,150 282,176 C290,150 310,124 350,112 C420,96 520,84 563,66 V92 C520,106 420,116 360,128 C318,140 296,166 282,196 C268,166 246,140 204,128 C144,116 43,106 0,92 Z" fill="var(--teal)"/>
    <path d="M0,0 H563 V66 C520,84 420,96 350,112 C310,124 290,150 282,176 C274,150 254,124 214,112 C144,96 43,84 0,66 Z" fill="var(--paper)"/>
    <path d="M0,240 C110,236 198,272 206,398 H192 C186,286 110,254 0,256 Z" fill="var(--teal)"/>
    <path d="M0,254 C108,252 184,284 190,398 H0 Z" fill="var(--paper)"/>
  </svg>
  <h1 class="headline">Join us for informative and personalized get together(s) to discuss the senior care home that we are opening</h1>
  <p class="intro">Harbridge Elder Homes is a unique care concept, designed around a social model which encourages “neighbors” to be as independent as possible, actively participate in life here, and interact with their fellow neighbors.</p>
  <div class="brand"><span class="brand__mark"></span><span>Harbridge<br>Elder Homes</span></div>
</section>

<section class="card card--back">
  <svg class="shapes" width="563" height="398" viewBox="0 0 563 398">
    <defs>
      <linearGradient id="lounge" x1="0" y1="0" x2="1" y2="1">
        <stop offset="0" stop-color="var(--photo-room-a)"/>
        <stop offset="1" stop-color="var(--photo-room-b)"/>
      </linearGradient>
    </defs>
    <path d="M0,0 H350 C342,40 320,66 290,92 C250,120 190,130 120,128 C70,128 30,140 0,160 Z" fill="url(#lounge)" role="img" aria-label="Photo: a bright living room with a large leather sectional sofa and garden windows"/>
    <path d="M0,150 C40,134 80,128 130,132 C200,136 258,124 300,96 C330,74 346,40 352,0 H364 C360,50 338,90 300,114 C250,146 190,150 130,150 C80,150 40,156 0,172 Z" fill="var(--teal)"/>
    <path d="M18,150 C60,134 100,132 140,136 C200,140 250,128 292,104 L300,114 C250,146 190,150 130,150 C90,150 52,156 26,164 Z" fill="#8a8a8a" opacity=".55"/>
  </svg>
  <div class="stamp">
    <div class="stamp__art" role="img" aria-label="Postage stamp illustration"></div>
    <svg class="postmark" width="148" height="92" viewBox="0 0 148 92" fill="none" stroke="#777" stroke-width="1">
      <path d="M6,22 C30,16 50,28 74,22 S118,16 142,22"/>
      <path d="M6,34 C30,28 50,40 74,34 S118,28 142,34"/>
      <path d="M6,46 C30,40 50,52 74,46 S118,40 142,46"/>
      <path d="M6,58 C30,52 50,64 74,58 S118,52 142,58"/>
      <path d="M6,70 C30,64 50,76 74,70 S118,64 142,70"/>
    </svg>
  </div>
  <p class="tagline">Our organization is sophisticated and built around warmth, care and individualized personal attention.</p>
  <div class="brand"><span class="brand__mark"></span><span>Harbridge<br>Elder Homes</span></div>
  <address class="contact">
    4870 Palmcrest Ave., Suite 210<br>
    Lanewood, HI 96999<br>
    Phone 808 555 01 72<br>
    Fax 808 555 0193<br>
    events@harbridge.example
  </address>
  <div class="address-lines"><span></span><span></span><span></span><span></span><span></span></div>
</section>

</body>
</html>
```